Creation of an elegant and modern turnkey Shopify website

Hello,

We are a new company specializing in the sale of above-ground pools. We want to create a turnkey website, ideally using Shopify. For now, we need a "showcase" site, not an e-commerce platform, with four tabs:

Home Page (an overall presentation of the company)
Our Products (an overview of all the above-ground pools we sell)
Our Projects (a page inspired by Photo Feed to showcase photos of our future projects)
Contact (a page with all our contact information and a contact form)

We are looking to create a highly visual, elegant, and modern website with vibrant splashes of color. We will provide the text, photos (along with instructions on where to place them on each page), and all other necessary information as attachments.

Thank you in advance for your proposals!

The Brisa Basin Team

Target Market(s)

Targeted at Swiss customers (a translator will need to be installed for different languages)

Industry/Entity Type

Sale of customised above-ground pools

Coding

Coded - Design and coding required

Font styles to use
Sans Serif

Colors
0094D4
00A9DD
6FCCEA
C7EBF8
E9F6FB
00AB8E
00BBA5
67D7C9
C6EFE9
E9F9F6

Requirements
Must have
• A stunning, elegant and modern look
Nice to have
• Inspiration from the colors of our logo throughout the site, but in an elegant way
Should not have
• An overly classic look for swimming pool sites

```html
<!DOCTYPE html>
<html lang="en">
<head>
<meta charset="utf-8">
<title>Brisa Basin – Premium Above Ground Pools</title>
<link href="https://fonts.googleapis.com/css2?family=Italiana&family=Poppins:wght@300;400;500&display=swap" rel="stylesheet">
<style>
:root{
  --aqua:#1cd3e6;
  --ink:#2b2b2b;
  --muted:#555;
  --band:#f3f3f3;
  --footer:#262626;
  --white:#fff;
  --line:#d6d6d6;
}
*{box-sizing:border-box;margin:0;padding:0}
html,body{width:1200px;height:3411px;overflow:hidden;background:var(--white)}
body{position:relative;font-family:'Poppins',sans-serif;color:var(--ink)}
.abs{position:absolute}
.serif{font-family:'Italiana',serif;font-weight:400;letter-spacing:.5px}
.center{text-align:center}

/* hero */
.hero{left:0;top:0;width:1200px;height:660px;background:linear-gradient(180deg,#34444a 0%,#2e5661 35%,#1f4d58 60%,#1a3b43 100%)}
.hero-wave{left:0;top:540px;width:1200px;height:125px}
.brand{left:135px;top:18px;color:var(--white);font-size:38px;line-height:38px}
.nav{top:50px;font-size:11px;letter-spacing:1.2px;color:var(--white)}
.nav.active{color:var(--aqua)}
.nav-rule{left:135px;top:107px;width:930px;height:1px;background:rgba(255,255,255,.3)}
.nav-icon{top:40px;width:32px;height:32px;border:1px solid rgba(255,255,255,.8);border-radius:50%}
.hero-title{left:0;width:1200px;top:222px;color:var(--white);font-size:42px;line-height:54px}
.hero-sub{left:0;width:1200px;top:340px;color:var(--white);font-size:12px}
.btn-ghost{left:526px;top:381px;width:111px;height:30px;border:1px solid var(--white);border-radius:15px;color:var(--white);font-size:10px;letter-spacing:1.2px;line-height:28px;text-align:center}

/* products */
.section-title{left:0;width:1200px;font-size:31px;text-align:center;color:var(--ink)}
.product-photo{top:764px;width:227px;height:312px}
.product-name{top:1092px;width:227px;font-size:14px;line-height:19px;text-align:center;color:var(--ink)}

/* why */
.why{left:0;top:1183px;width:1200px;height:642px;background:var(--band)}
.arch{left:122px;top:1262px;width:391px;height:422px;border-radius:196px 196px 0 0;background:linear-gradient(160deg,#a9dfe2,#8fd3d9 50%,#b7e5e6)}
.round-photo{left:449px;top:1379px;width:188px;height:188px;border-radius:50%;border:5px solid var(--white);background:linear-gradient(160deg,#3c5a6d,#3a9ac7 55%,#7bd0ea)}
.why-title{left:682px;top:1244px;font-size:31px;line-height:38px}
.step-line{left:700px;top:1362px;width:1px;height:344px;background:var(--aqua)}
.step-dot{left:683px;width:36px;height:36px;border-radius:50%;background:var(--aqua);color:var(--white);font-size:12px;font-weight:500;line-height:36px;text-align:center}
.step-title{left:732px;font-size:15px}
.step-text{left:735px;width:345px;font-size:10.5px;line-height:16px;color:var(--muted)}

/* projects */
.project-photo{top:1943px;height:363px}
.project-name{top:2321px;width:318px;text-align:center;font-size:14px}
.arrow{top:2142px;width:34px;height:34px;border:1px solid var(--white);border-radius:50%}
.btn-fill{left:544px;top:2388px;width:112px;height:29px;border-radius:15px;background:var(--aqua);color:var(--white);font-size:10px;letter-spacing:1.2px;line-height:29px;text-align:center}

/* services */
.services{left:0;top:2480px;width:1200px;height:321px;background:var(--band)}
.divider{top:2563px;width:1px;height:189px;background:var(--line)}
.svc-icon{top:2528px;width:40px;height:48px}
.svc-title{top:2598px;width:290px;font-size:18px;letter-spacing:.5px;text-align:center}
.svc-text{top:2634px;width:280px;font-size:10.5px;line-height:16.5px;text-align:center;color:var(--muted)}

/* newsletter */
.news-title{left:0;width:1200px;top:2856px;font-size:30px;line-height:39px;text-align:center}
.news-sub{left:0;width:1200px;top:2947px;font-size:11px;text-align:center;color:var(--muted)}
.email{left:377px;top:2992px;width:325px;height:31px;border:1px solid var(--line);border-radius:16px;font-size:8px;color:#999;padding-left:22px;line-height:31px}
.subscribe{left:711px;top:2992px;width:111px;height:31px;border-radius:16px;background:var(--aqua);color:var(--white);font-size:9.5px;letter-spacing:1.2px;line-height:31px;text-align:center}

/* footer */
.footer{left:0;top:3086px;width:1200px;height:325px;background:var(--footer)}
.foot-head{top:3148px;color:var(--white);font-size:15px}
.foot-link{left:120px;color:var(--white);font-size:11px}
.foot-text{color:var(--white);font-size:11px;line-height:15px}
.foot-circle{width:32px;height:32px;border:1px solid var(--white);border-radius:50%}
.foot-brand{left:760px;top:3120px;width:340px;color:var(--white);font-size:112px;line-height:118px;text-align:center}
.foot-rule{left:120px;top:3326px;width:661px;height:1px;background:#555}
.copyright{left:120px;top:3357px;color:var(--white);font-size:10.5px}
</style>
</head>
<body>

<!-- Hero -->
<div class="abs hero" role="img" aria-label="Resort pool at dusk with lounge chairs in the water and palm trees along the sea"></div>
<svg class="abs hero-wave" viewBox="0 0 1200 125" preserveAspectRatio="none" aria-hidden="true">
  <path d="M0 63 C90 30 150 5 260 13 C400 25 480 110 620 108 C760 106 880 -5 1010 12 C1090 22 1150 40 1200 52 L1200 125 L0 125 Z" fill="#fff"/>
</svg>

<div class="abs brand serif">BRISA<br>BASIN</div>
<div class="abs nav active" style="left:532px">HOME</div>
<div class="abs nav" style="left:609px">OUR PRODUCT</div>
<div class="abs nav" style="left:735px">OUR PROJECT</div>
<div class="abs nav" style="left:857px">CONTACT US</div>
<svg class="abs nav-icon" style="left:957px" viewBox="0 0 32 32" aria-label="Search"><circle cx="15" cy="15" r="5" fill="none" stroke="#fff" stroke-width="1.3"/><line x1="19" y1="19" x2="22" y2="22" stroke="#fff" stroke-width="1.3"/></svg>
<svg class="abs nav-icon" style="left:1001px" viewBox="0 0 32 32" aria-label="Photo feed"><rect x="10" y="10" width="12" height="12" rx="3" fill="none" stroke="#fff" stroke-width="1.3"/></svg>
<svg class="abs nav-icon" style="left:1044px" viewBox="0 0 32 32" aria-label="Account"><circle cx="16" cy="13" r="3.2" fill="none" stroke="#fff" stroke-width="1.3"/><path d="M10.5 22 C11 18 21 18 21.5 22 Z" fill="none" stroke="#fff" stroke-width="1.3"/></svg>
<div class="abs nav-rule"></div>

<h1 class="abs hero-title serif center">TRANSFORM YOUR GARDEN WITH OUR<br>PREMIUM&nbsp; ABOVE GROUND POOLS</h1>
<p class="abs hero-sub">Achieve your dreams with our custom, tailor-made above-ground pools.</p>
<div class="abs btn-ghost">OUR WORK</div>

<!-- Products -->
<h2 class="abs section-title serif" style="top:702px">MOST WANTED OUR PRODUCT</h2>
<div class="abs product-photo" style="left:120px;background:linear-gradient(180deg,#3d7a45 0%,#5aa65a 30%,#6fd3e8 45%,#4fc6e6 100%)" role="img" aria-label="Turquoise garden pool with stepping stones and a pergola"></div>
<div class="abs product-photo" style="left:364px;background:linear-gradient(180deg,#e6ebee 0%,#6d9a5b 35%,#4e5d5c 60%,#2f98d6 85%,#3aa6e0 100%)" role="img" aria-label="Pool with a stone waterfall and palm trees"></div>
<div class="abs product-photo" style="left:607px;background:linear-gradient(180deg,#cfe4ee 0%,#7a6a56 30%,#2f2f2f 55%,#38b7d5 70%,#e5e5e3 100%)" role="img" aria-label="Sun loungers under a striped umbrella beside a pool"></div>
<div class="abs product-photo" style="left:850px;background:linear-gradient(180deg,#4c5c60 0%,#6f9fa9 40%,#b9dbe3 70%,#d9ecf0 100%)" role="img" aria-label="Guest relaxing in a bubbling mini spa"></div>
<div class="abs product-name" style="left:120px">Aluminium Pools</div>
<div class="abs product-name" style="left:364px">Ground Pools with<br>Aluminium and Wood</div>
<div class="abs product-name" style="left:607px">Galvanized Steel Pools<br>Composite Wood Coverings</div>
<div class="abs product-name" style="left:850px">Mini Pool Spa</div>

<!-- Why choose -->
<div class="abs why"></div>
<div class="abs arch" role="img" aria-label="Aerial view of a swimmer on a pink float in clear water"></div>
<div class="abs round-photo" role="img" aria-label="Curved pool edge lined with sun loungers"></div>
<h2 class="abs why-title serif">WHY CHOOSE OUR<br>ABOVE GROUND POOLS?</h2>
<div class="abs step-line"></div>

<div class="abs step-dot" style="top:1344px">1</div>
<div class="abs step-title" style="top:1350px">Superior Quality:</div>
<p class="abs step-text" style="top:1380px">Each pool is constructed with high-quality materials, ensuring exceptional durability and strength.</p>

<div class="abs step-dot" style="top:1430px">2</div>
<div class="abs step-title" style="top:1436px">Elegant Design:</div>
<p class="abs step-text" style="top:1466px">Our pools come in a variety of styles and finishes, seamlessly blending into any garden setting.</p>

<div class="abs step-dot" style="top:1516px">3</div>
<div class="abs step-title" style="top:1522px">Custom and Tailor-Made:</div>
<p class="abs step-text" style="top:1552px">Create the pool of your dreams with our customization options, tailored to your specific tastes and needs.</p>

<div class="abs step-dot" style="top:1602px">4</div>
<div class="abs step-title" style="top:1608px">Easy Installation:</div>
<p class="abs step-text" style="top:1638px">Enjoy your new oasis quickly with our simple and fast installation process.</p>

<div class="abs step-dot" style="top:1688px">5</div>
<div class="abs step-title" style="top:1694px">Constant Innovation:</div>
<p class="abs step-text" style="top:1724px">We incorporate the latest technologies to provide you with an optimal and safe swimming experience.</p>

<!-- Projects -->
<h2 class="abs section-title serif" style="top:1878px">OUR BEST PROJECTS</h2>
<div class="abs project-photo" style="left:0;width:69px;background:linear-gradient(180deg,#8fd8e0,#4fbfcf)" role="img" aria-label="Edge of a pool project photo"></div>
<div class="abs project-photo" style="left:95px;width:318px;background:linear-gradient(135deg,#8cc8e4 0%,#6fb6dc 45%,#a98565 60%,#b49077 100%)" role="img" aria-label="Wooden pool deck with pebbles and a steel ladder"></div>
<div class="abs project-photo" style="left:440px;width:319px;background:linear-gradient(180deg,#6f7176 0%,#8a8b8f 45%,#6a4a3c 72%,#2f95d6 85%,#3aa8e0 100%)" role="img" aria-label="Two loungers against a stone gabion wall by the pool"></div>
<div class="abs project-photo" style="left:785px;width:320px;background:linear-gradient(180deg,#2a6fa0 0%,#2e9ad6 45%,#c4306e 75%,#d9d3c8 100%)" role="img" aria-label="Pink towel, sunglasses, hat and a drink beside the pool"></div>
<div class="abs project-photo" style="left:1132px;width:68px;background:linear-gradient(180deg,#8fd8e0,#5dbfc9)" role="img" aria-label="Edge of a pool project photo"></div>
<svg class="abs arrow" style="left:72px" viewBox="0 0 34 34" aria-label="Previous"><line x1="-18" y1="17" x2="24" y2="17" stroke="#fff" stroke-width="1.2"/><polyline points="-12,12 -18,17 -12,22" fill="none" stroke="#fff" stroke-width="1.2"/></svg>
<svg class="abs arrow" style="left:1094px;overflow:visible" viewBox="0 0 34 34" aria-label="Next"><line x1="10" y1="17" x2="52" y2="17" stroke="#fff" stroke-width="1.2"/><polyline points="46,12 52,17 46,22" fill="none" stroke="#fff" stroke-width="1.2"/></svg>
<div class="abs project-name" style="left:95px">Lorem Ipsum Dummy text</div>
<div class="abs project-name" style="left:440px">Lorem Ipsum Dummy text</div>
<div class="abs project-name" style="left:785px">Lorem Ipsum Dummy text</div>
<div class="abs btn-fill">OUR WORK</div>

<!-- Services -->
<div class="abs services"></div>
<div class="abs divider" style="left:437px"></div>
<div class="abs divider" style="left:763px"></div>

<svg class="abs svc-icon" style="left:251px" viewBox="0 0 40 48" aria-hidden="true" fill="none" stroke="var(--aqua)" stroke-width="1.4">
  <circle cx="17" cy="20" r="6"/><path d="M6 40 C6 30 28 30 28 40"/><rect x="2" y="40" width="30" height="5"/><path d="M26 5 h12 v9 h-8 l-4 3z"/>
</svg>
<svg class="abs svc-icon" style="left:580px" viewBox="0 0 40 48" aria-hidden="true" fill="none" stroke="var(--aqua)" stroke-width="1.4">
  <path d="M20 4 L35 10 V22 C35 32 28 40 20 44 C12 40 5 32 5 22 V10 Z"/><polyline points="13,23 18,28 28,17"/>
</svg>
<svg class="abs svc-icon" style="left:905px" viewBox="0 0 40 48" aria-hidden="true" fill="none" stroke="var(--aqua)" stroke-width="1.4">
  <rect x="4" y="4" width="30" height="38" rx="2"/><line x1="4" y1="12" x2="34" y2="12"/><line x1="10" y1="20" x2="28" y2="20"/><line x1="10" y1="27" x2="28" y2="27"/><line x1="10" y1="34" x2="22" y2="34"/>
</svg>

<h3 class="abs svc-title" style="left:129px;font-weight:400">PERSONALIZED SERVICES</h3>
<p class="abs svc-text" style="left:134px">We understand that every garden and client is unique. That's why we offer personalized services, from design to installation and after-sales support. Our team of experts is here to answer all your questions and guide you throughout your project.</p>
<h3 class="abs svc-title" style="left:455px;font-weight:400">GUARANTEED SATISFACTION</h3>
<p class="abs svc-text" style="left:460px">Your satisfaction is our top priority. We are committed to providing you with exceptional service and the highest quality products. Join our community of satisfied customers who are already enjoying their custom above-ground pools. 10-Year Warranty!</p>
<h3 class="abs svc-title" style="left:780px;font-weight:400">CONTACT US TODAY</h3>
<p class="abs svc-text" style="left:785px">Don't wait any longer to transform your garden into a wellness oasis. Contact us today to discover our range of customizable above-ground pools and get a tailored quote. Dive into a world of infinite possibilities with Us.</p>

<!-- Newsletter -->
<h2 class="abs news-title serif">WE BRING YOUR POOL DREAMS TO LIFE<br>SUBSCRIBE OUR NEWSLETTER</h2>
<p class="abs news-sub">Be the first to know about new collections and exclusive offers.</p>
<div class="abs email">Enter Your Email</div>
<div class="abs subscribe">SUBSCRIBE</div>

<!-- Footer -->
<div class="abs footer"></div>
<div class="abs foot-head serif" style="left:120px">QUICK LINKS</div>
<div class="abs foot-link" style="top:3181px">Home</div>
<div class="abs foot-link" style="top:3199px">Our Product</div>
<div class="abs foot-link" style="top:3218px">Our Project</div>
<div class="abs foot-link" style="top:3237px">Contact Us</div>

<div class="abs foot-head serif" style="left:297px">CONTACT INFO</div>
<svg class="abs foot-circle" style="left:297px;top:3200px" viewBox="0 0 32 32" aria-label="Address"><path d="M16 24 C12 19 11 16.5 11 14.5 A5 5 0 0 1 21 14.5 C21 16.5 20 19 16 24Z" fill="#fff"/><circle cx="16" cy="14.5" r="1.8" fill="#262626"/></svg>
<div class="abs foot-text" style="left:338px;top:3183px">Lucien Morel Chemin des Saules<br>27 Aigle<br>1860 Vaud</div>
<svg class="abs foot-circle" style="left:297px;top:3256px" viewBox="0 0 32 32" aria-label="Phone"><path d="M11 9.5 L13.5 9 L15 13 L13.3 14.3 C14.3 16.5 15.5 17.7 17.7 18.7 L19 17 L23 18.5 L22.5 21 C16 22 10 16 11 9.5Z" fill="#fff"/></svg>
<div class="abs foot-text" style="left:338px;top:3264px">079 000 12 34</div>

<div class="abs foot-head serif" style="left:576px">SOCIAL LINKS</div>
<svg class="abs foot-circle" style="left:571px;top:3200px" viewBox="0 0 32 32" aria-hidden="true"><circle cx="16" cy="16" r="4" fill="none" stroke="#fff" stroke-width="1.3"/></svg>
<div class="abs foot-text" style="left:611px;top:3209px">Photo Feed</div>

<div class="abs foot-brand serif">BRISA<br>BASIN</div>
<div class="abs foot-rule"></div>
<div class="abs copyright">©Copyright All Right Reserved. The Brisa.2024</div>

</body>
</html>
```